The Plate Compass

Cutting Through the Noise to What Actually Works.

Nutrition book

Target Market(s)

People looking to be or get healthy and eat right.

```html
<!DOCTYPE html>
<html lang="en">
<head>
<meta charset="utf-8">
<title>Cutting Through the Noise – The Plate Compass</title>
<link href="https://fonts.googleapis.com/css2?family=Anton&family=Permanent+Marker&family=Oswald:wght@500;600&family=Barlow:wght@400;500&display=swap" rel="stylesheet">
<style>
  :root{
    --page:#ececec;
    --cover:#ebe7df;
    --ink:#141414;
    --yellow:#f2c623;
    --green:#1f7a2c;
    --red:#c23a22;
    --gold:#d39a18;
    --blue:#1d5aa6;
    --charcoal:#2a2a2a;
    --muted:#3a3a3a;
  }
  *{margin:0;padding:0;box-sizing:border-box}
  html,body{width:1200px;height:800px;overflow:hidden;background:var(--page)}
  .cover{position:absolute;left:351px;top:20px;width:498px;height:760px;background:var(--cover);overflow:hidden;color:var(--ink);font-family:'Barlow',sans-serif}
  .cover span,.cover p{white-space:nowrap}

  .title{font-size:16px;font-weight:400}
  .title-band{position:absolute;left:38px;top:22px;width:424px;height:42px;background:var(--yellow);transform:rotate(-4deg);border-radius:3px 12px 4px 14px}
  .title-top{position:absolute;left:66px;top:14px;font-family:'Permanent Marker','Anton',sans-serif;font-size:40px;line-height:1;transform:rotate(-4deg);transform-origin:left bottom}
  .title-main{position:absolute;left:50px;top:74px;font-family:'Anton',sans-serif;font-size:94px;line-height:1;letter-spacing:-1px}
  .title-main .noise{margin-left:12px}
  .strike{position:absolute;left:204px;top:86px;width:236px;height:40px}
  .title-sub{position:absolute;left:61px;top:178px;font-family:'Anton',sans-serif;font-size:24px;line-height:1}
  .title-accent{position:absolute;left:170px;top:156px;font-family:'Permanent Marker','Anton',sans-serif;font-size:34px;line-height:1;color:var(--green);transform:rotate(-5deg);transform-origin:left bottom}
  .accent-line{position:absolute;left:188px;top:188px;width:260px;height:14px}

  .stack-art{position:absolute;left:189px;top:244px;width:150px;height:432px;border-radius:60px 60px 20px 20px;background:linear-gradient(180deg,#6f8d3a 0%,#b98a4c 22%,#4e8a34 42%,#c2562f 58%,#b49a72 70%,#9d9d9d 82%,#505050 100%)}
  .noise-art{position:absolute;left:346px;top:222px;width:152px;height:442px;background:linear-gradient(180deg,rgba(60,60,60,.12) 0%,rgba(40,40,40,.5) 50%,rgba(80,80,80,.4) 100%);border-radius:40px 0 0 30px}
  .noise-tag{position:absolute;font-family:'Oswald',sans-serif;font-weight:600;font-size:10px;line-height:1.05;color:var(--charcoal);transform:rotate(-12deg);text-transform:uppercase;text-align:center}
  .pile-tag{position:absolute;font-family:'Oswald',sans-serif;font-weight:500;font-size:10px;background:#f4f2ee;color:var(--charcoal);padding:1px 4px;text-transform:uppercase}

  .hierarchy{position:absolute;left:40px;top:0;list-style:none}
  .tier{position:absolute;left:0;width:190px;height:40px}
  .tier .icon{position:absolute;left:0;top:0;width:38px;height:38px;border-radius:50%}
  .tier .name{position:absolute;left:46px;top:2px;font-family:'Oswald',sans-serif;font-weight:600;font-size:14px;line-height:18px}
  .tier .name svg{vertical-align:middle;margin-left:6px}
  .tier .note{position:absolute;left:59px;top:21px;font-size:9.5px;color:var(--muted)}
  .t-cal{top:254px}.t-cal .icon{background:var(--green)}.t-cal .name{color:var(--green)}
  .t-pro{top:322px}.t-pro .icon{background:var(--red)}.t-pro .name{color:var(--red)}
  .t-qual{top:390px}.t-qual .icon{background:var(--green)}.t-qual .name{color:var(--green)}
  .t-time{top:460px}.t-time .icon{background:var(--gold)}.t-time .name{color:var(--gold)}
  .t-supp{top:527px}.t-supp .icon{background:var(--blue)}.t-supp .name{color:var(--blue)}
  .t-noise{top:592px}.t-noise .icon{background:var(--charcoal)}.t-noise .name{color:var(--ink)}
  .num{color:var(--ink)}

  .tagline{position:absolute;left:0;width:100%;top:686px;text-align:center;font-size:10px;letter-spacing:1.6px;font-weight:500}
  .tag-rule{position:absolute;left:182px;top:705px;width:122px;height:2px;background:var(--green)}
  .footer-rule{position:absolute;top:727px;height:1px;background:var(--green)}
  .footer-rule.left{left:118px;width:118px}.footer-rule.right{left:262px;width:118px}
  .footer-dot{position:absolute;left:244px;top:723px;width:9px;height:9px;border-radius:50%;background:var(--green)}
  .imprint{position:absolute;left:0;width:100%;top:740px;text-align:center;font-size:8px;letter-spacing:1.4px;font-weight:500}
</style>
</head>
<body>
<main class="cover">
  <div class="title-band"></div>
  <h1 class="title">
    <span class="title-top">CUTTING THROUGH</span>
    <span class="title-main">THE<span class="noise">NOISE</span></span>
    <span class="title-sub">TO WHAT</span>
    <span class="title-accent">ACTUALLY WORKS.</span>
  </h1>
  <svg class="strike" viewBox="0 0 236 40"><path d="M2 24 L234 12" stroke="#141414" stroke-width="5" fill="none"/><path d="M8 30 L228 19" stroke="#ebe7df" stroke-width="2" fill="none"/></svg>
  <svg class="accent-line" viewBox="0 0 260 14"><path d="M2 12 Q130 2 258 4" stroke="#1f7a2c" stroke-width="3" fill="none" stroke-linecap="round"/></svg>

  <div class="stack-art" role="img" aria-label="Stacked bowls of food: avocado, berries and nuts on top, grilled chicken and eggs, vegetables, grain salad, supplements, resting on crumpled diet-trend papers"></div>
  <div class="noise-art" role="img" aria-label="Swirl of dark scribbled lines flowing into a metal trash bin"></div>
  <span class="noise-tag" style="left:424px;top:280px">Fad Diets</span>
  <span class="noise-tag" style="left:380px;top:312px">Misinformation</span>
  <span class="noise-tag" style="left:384px;top:352px">ClipFeed Trends</span>
  <span class="noise-tag" style="left:390px;top:412px">Quick Fixes</span>
  <span class="noise-tag" style="left:392px;top:456px">Conflicting<br>Advice</span>
  <span class="noise-tag" style="left:412px;top:494px">Myths</span>
  <span class="pile-tag" style="left:184px;top:608px;transform:rotate(-28deg)">Low Carb?</span>
  <span class="pile-tag" style="left:310px;top:588px;transform:rotate(10deg)">Detox?</span>
  <span class="pile-tag" style="left:318px;top:632px;transform:rotate(22deg)">Superfoods?</span>
  <span class="pile-tag" style="left:189px;top:652px;transform:rotate(-8deg)">Ketox?</span>

  <ol class="hierarchy">
    <li class="tier t-cal">
      <svg class="icon" viewBox="0 0 38 38"><path d="M19 9 C24 15 26 19 25 23 A6 6 0 0 1 13 23 C12 19 15 17 16 13 C18 16 19 16 19 9Z" fill="#fff"/></svg>
      <span class="name"><span class="num">1.</span> CALORIES<svg width="30" height="8" viewBox="0 0 30 8"><path d="M0 4H27M23 1L28 4L23 7" stroke="#141414" fill="none" stroke-width="1.2"/></svg></span>
      <span class="note">Most Important</span>
    </li>
    <li class="tier t-pro">
      <svg class="icon" viewBox="0 0 38 38"><path d="M13 27 L13 15 Q15 10 19 11 L19 15 L16 16 L17 21 Q22 17 26 21 Q26 27 20 27Z" fill="#fff"/></svg>
      <span class="name"><span class="num">2.</span> PROTEIN<svg width="30" height="8" viewBox="0 0 30 8"><path d="M0 4H27M23 1L28 4L23 7" stroke="#c23a22" fill="none" stroke-width="1.2"/></svg></span>
      <span class="note">Builds &amp; Repairs</span>
    </li>
    <li class="tier t-qual">
      <svg class="icon" viewBox="0 0 38 38"><path d="M12 27 Q12 12 27 11 Q27 26 12 27Z" fill="#fff"/><path d="M12 27 L22 17" stroke="#1f7a2c" stroke-width="1.5"/></svg>
      <span class="name"><span class="num">3.</span> FOOD QUALITY<svg width="22" height="8" viewBox="0 0 22 8"><path d="M0 4H19M15 1L20 4L15 7" stroke="#1f7a2c" fill="none" stroke-width="1.2"/></svg></span>
      <span class="note">Better Nutrients</span>
    </li>
    <li class="tier t-time">
      <svg class="icon" viewBox="0 0 38 38"><circle cx="19" cy="19" r="9" fill="none" stroke="#fff" stroke-width="2"/><path d="M19 13V19L23 22" stroke="#fff" stroke-width="2" fill="none"/></svg>
      <span class="name"><span class="num">4.</span> MEAL TIMING<svg width="20" height="8" viewBox="0 0 20 8"><path d="M0 4H17M13 1L18 4L13 7" stroke="#d39a18" fill="none" stroke-width="1.2"/></svg></span>
      <span class="note">Optimizes Results</span>
    </li>
    <li class="tier t-supp">
      <svg class="icon" viewBox="0 0 38 38"><rect x="10" y="15" width="18" height="8" rx="4" transform="rotate(-45 19 19)" fill="none" stroke="#fff" stroke-width="2"/><path d="M16 16L22 22" stroke="#fff" stroke-width="2"/></svg>
      <span class="name"><span class="num">5.</span> SUPPLEMENTS<svg width="20" height="8" viewBox="0 0 20 8"><path d="M0 4H17M13 1L18 4L13 7" stroke="#1d5aa6" fill="none" stroke-width="1.2"/></svg></span>
      <span class="note">Fills the Gaps</span>
    </li>
    <li class="tier t-noise">
      <svg class="icon" viewBox="0 0 38 38"><path d="M11 16H15L20 12V26L15 22H11Z" fill="#fff"/><path d="M23 15L29 23M29 15L23 23" stroke="#fff" stroke-width="2"/></svg>
      <span class="name"><span class="num">6.</span> NOISE<svg width="30" height="8" viewBox="0 0 30 8"><path d="M0 4H27M23 1L28 4L23 7" stroke="#141414" fill="none" stroke-width="1.2"/></svg></span>
      <span class="note">Least Important</span>
    </li>
  </ol>

  <p class="tagline">SIMPLE. EVIDENCE - BASED. REAL RESULTS.</p>
  <div class="tag-rule"></div>
  <div class="footer-rule left"></div>
  <div class="footer-dot"></div>
  <div class="footer-rule right"></div>
  <p class="imprint">THE PLATE COMPASS</p>
</main>
</body>
</html>
```